Brivora Collective Business Card Design

We need a business card design for Brivora Collective. We are a healthcare recruiting, wellness and education company. We partner with medical facilities to find quality candidates. We also offer free wellness courses.
The final design should communicate an emphasis on recruiting and wellness
The main purpose of the business card is to utilized it for networking events, give to hospitals, executives, VCs surgery centers and clinics. I want it to be sleek, clean, use of our brand colors and professional.

```html
<!DOCTYPE html>
<html lang="en">
<head>
<meta charset="UTF-8">
<title>Brivora Collective — Business Card</title>
<link href="https://fonts.googleapis.com/css2?family=Montserrat:wght@400;500&display=swap" rel="stylesheet">
<style>
  :root {
    --backdrop: #b3b3b3;
    --teal-deep: #005c55;
    --teal-bright: #10998a;
    --teal-mist: #9cd8d8;
    --paper: #ffffff;
  }
  * { margin: 0; padding: 0; box-sizing: border-box; }
  html, body {
    width: 1200px; height: 917px; overflow: hidden;
    background: var(--backdrop);
    font-family: "Montserrat", sans-serif;
  }
  .canvas { position: relative; width: 1200px; height: 917px; }

  .card {
    position: absolute;
    width: 544px; height: 311px;
    overflow: hidden;
  }

  /* Front side */
  .card--front {
    left: 324px; top: 91px;
    background: linear-gradient(100deg, var(--teal-bright) 0%, #06776d 50%, var(--teal-deep) 100%);
    display: flex; align-items: center; justify-content: center;
  }
  .card--front .brand-name {
    color: var(--paper);
    font-size: 34px; font-weight: 500;
    letter-spacing: 0.5px;
  }

  /* Back side */
  .card--back {
    left: 328px; top: 507px;
    background: var(--paper);
  }
  .back-waves { position: absolute; inset: 0; width: 100%; height: 100%; }
  .card--back .brand-name {
    position: absolute; left: 0; right: 0; top: 98px;
    text-align: center;
    color: var(--teal-deep);
    font-size: 28px; font-weight: 500;
  }

  .contact-list {
    position: absolute; left: 45px; top: 193px;
    list-style: none;
  }
  .contact-item {
    display: flex; align-items: center;
    height: 22px; margin-bottom: 10px;
    color: var(--paper);
    font-size: 12px; letter-spacing: 0.4px;
  }
  .contact-icon { width: 22px; height: 22px; margin-right: 12px; flex: none; }

  .holder {
    position: absolute; left: 311px; top: 216px;
    color: var(--paper);
  }
  .holder-name { font-size: 21px; font-weight: 400; letter-spacing: 0.8px; line-height: 1; }
  .holder-title { font-size: 10.5px; margin-top: 1px; }
</style>
</head>
<body>
<div class="canvas">

  <section class="card card--front">
    <span class="brand-name">Brivora Collective</span>
  </section>

  <section class="card card--back">
    <svg class="back-waves" viewBox="0 0 997 569" preserveAspectRatio="none" aria-hidden="true">
      <path d="M0 241 Q500 343 997 241 L997 569 L0 569 Z" fill="var(--teal-mist)"/>
      <path d="M0 291 Q470 362 997 242 L997 569 L0 569 Z" fill="var(--teal-deep)"/>
    </svg>

    <span class="brand-name">Brivora Collective</span>

    <ul class="contact-list">
      <li class="contact-item">
        <svg class="contact-icon" viewBox="0 0 22 22" aria-hidden="true">
          <circle cx="11" cy="11" r="10" fill="none" stroke="#fff" stroke-width="1.2"/>
          <path d="M8 6.5c-.8.4-1.2 1-1 2 .6 2.8 3 5.6 5.8 6.6 1 .3 1.7-.1 2.2-.9l-1.7-1.4-1.1.7c-1.3-.6-2.4-1.8-2.9-3.1l.8-1z" fill="#fff"/>
        </svg>
        <span>012 345 7890</span>
      </li>
      <li class="contact-item">
        <svg class="contact-icon" viewBox="0 0 22 22" aria-hidden="true">
          <circle cx="11" cy="11" r="10" fill="none" stroke="#fff" stroke-width="1.2"/>
          <rect x="6" y="8" width="10" height="6.5" fill="#fff"/>
          <path d="M6 8l5 4 5-4M6 14.5l3.6-3.4M16 14.5l-3.6-3.4" fill="none" stroke="var(--teal-deep)" stroke-width="0.8"/>
        </svg>
        <span>info@website.com</span>
      </li>
      <li class="contact-item">
        <svg class="contact-icon" viewBox="0 0 22 22" aria-hidden="true">
          <circle cx="11" cy="11" r="10" fill="none" stroke="#fff" stroke-width="1.2"/>
          <path d="M9 6v9l2-2 1.4 3 1-.5-1.3-2.9 2.8-.2z" fill="#fff"/>
        </svg>
        <span>www.website.com</span>
      </li>
    </ul>

    <div class="holder">
      <p class="holder-name">YOUR NAME</p>
      <p class="holder-title">Title</p>
    </div>
  </section>

</div>
</body>
</html>
```